HTML Digital Sign layout and code (one page)...save us from the 60's!

Digital Sign for Headquarters Entrance

HTML Digital Sign layout (one page)...save us from the 60's!

Good Day Designers!

We have decided to install Digital Signage in our headquarters building that will replace the “felt boards” that the administrative staff use at our building entrances.

Instead of the information being displayed on the archaic sign boards, it will be presented on a landscaped 50inch LCD screen running at 1920x1080

We are looking for a one page HTML design that encompass the following elements:

+ Our Logo
+ Our Company Name (Vorlan Aerotek)
+ Our "Tag Line" - "Progress Shaped By Practice, Quality Shaped By Dedication"
+ Date and Time
+ A space for Today’s Birthdays (which could be up to 4 people)
+ A space for Today’s Anniversaries (which could be up to 4 people)
+ A space for Today’s Visitor (which could be up to 2 people)
+ A space for a Picture of the Day
+ A space for Weather Forecast (perhaps a graphic)
+ A small "banner" section or strip for scrolling Notices / Alerts (perhaps at the bottom of the page?)

The deliverables for the layout need to include the HTML, applicable CSS, HTML code, etc. We need this to be relatively turnkey.

I have included in the contest package a hi-res JPG and AI for our Company Logo.

From a color pallet perspective:

Light Blue:
RGB - 21, 191,242
HEX - #15BFF2

Dark Blue:
RGB - 0, 70, 154
HEX - #00469A

Additionally, I have done a contest like this before (for another company I was at) and have included a screen shot of that final display.

PLEASE NOTE: IT DOES NOT HAVE TO LOOK EXACTLY LIKE THE ATTACHED SCREEN SHOT FROM THE PREVIOUS CONTEST. Including the screenshot was just to give you a general idea of some inspiration and objectives.

Feedback and questions are encouraged.

Target Market(s)

Our Employees

Industry/Entity Type

Digital

Number of Pages Required

1 page

Requirements
Must have
• + Our Logo
• + Our Company Name (Vorlan Aerotek)
• + Our "Tag Line" - "Progress Shaped By Practice, Quality Shaped By Dedication"
• + Date and Time
• + A space for Today’s Birthdays (which could be up to 4 people)
• + A space for Today’s Anniversaries (which could be up to 4 people)
• + A space for Today’s Visitor (which could be up to 2 people)
• + A space for a Picture of the Day
• + A space for Weather Forecast (perhaps a graphic)
• + A small "banner" section or strip for scrolling Notices / Alerts (perhaps at the bottom of the page?)

```html
<!DOCTYPE html>
<html lang="en">
<head>
<meta charset="utf-8">
<title>Vorlan Aerotek – Entrance Display</title>
<link rel="stylesheet" href="https://fonts.googleapis.com/css2?family=Cinzel:wght@600&family=Mulish:wght@600;700;800&family=Questrial&display=swap">
<style>
  :root {
    --brand-dark: #1d3a8f;
    --brand-deep: #16296f;
    --brand-mid: #3d62bd;
    --brand-light: #15bff2;
    --sky-top: #5fd3f7;
    --sky-mid: #a9e6fb;
    --sky-pale: #e4f7fe;
    --panel-fill: rgba(236, 238, 240, 0.95);
    --panel-line: #48c6f0;
    --ink: #1b1b1b;
    --ink-soft: #3d3d3d;
    --caption: #6d6d6d;
    --photo-warm: #e6a53a;
    --photo-glow: #f6d36f;
    --alert-yellow: #f6c21a;
    --white: #ffffff;
  }
  * { box-sizing: border-box; margin: 0; padding: 0; }
  html, body { width: 1200px; height: 675px; overflow: hidden; }
  body {
    position: relative;
    font-family: "Mulish", sans-serif;
    color: var(--ink);
    background:
      radial-gradient(circle at 18% 90%, rgba(255,255,255,0.55) 0, rgba(255,255,255,0) 18%),
      radial-gradient(circle at 62% 28%, rgba(255,255,255,0.6) 0, rgba(255,255,255,0) 22%),
      radial-gradient(circle at 92% 12%, rgba(255,255,255,0.5) 0, rgba(255,255,255,0) 14%),
      linear-gradient(160deg, var(--sky-top) 0%, var(--sky-mid) 45%, var(--sky-pale) 75%, var(--sky-mid) 100%);
  }
  .abs { position: absolute; }

  /* Header */
  .brand { left: 52px; top: 70px; display: flex; align-items: center; gap: 12px; }
  .brand-dot { width: 20px; height: 20px; border-radius: 50%; background: var(--brand-dark); }
  .brand-name { font-family: "Mulish", sans-serif; font-weight: 800; font-size: 30px; color: var(--brand-dark); letter-spacing: 0.5px; }
  .tagline {
    left: 300px; top: 58px; width: 540px; text-align: center;
    font-family: "Cinzel", serif; font-weight: 600; font-size: 24px; line-height: 41px;
    color: var(--brand-dark); text-shadow: 0 0 4px var(--white), 0 0 2px var(--white);
  }
  .clock { left: 874px; top: 50px; font-family: "Mulish", sans-serif; font-weight: 700; font-size: 28px; line-height: 52px; color: var(--brand-dark); }

  /* Panels */
  .panel { background: var(--panel-fill); border: 1.5px solid var(--panel-line); }
  .band {
    display: flex; align-items: center; gap: 12px;
    background: linear-gradient(180deg, var(--brand-mid) 0%, var(--brand-dark) 55%, var(--brand-deep) 100%);
    color: var(--white); font-weight: 700; font-size: 26px; border-radius: 10px;
    box-shadow: 0 3px 4px rgba(0,0,0,0.25);
  }
  .band-icon { width: 34px; height: 30px; border-radius: 5px; flex: none; }
  .icon-camera { background: linear-gradient(135deg, #f4f4f4, #8fc6e9); }
  .icon-cake { background: linear-gradient(180deg, #f6c56a, #a0602a); }
  .icon-glasses { background: linear-gradient(180deg, #fde39a, #d93a2b); }
  .icon-card { background: linear-gradient(90deg, #e23a3a 0 40%, #f5f5f5 40%); }
  .icon-sun { background: linear-gradient(135deg, #ffd23c, #f5f5f5); border-radius: 50%; }
  .tab-strip { background: #e9ebee; border-radius: 6px 6px 0 0; }

  .name-list { list-style: none; font-weight: 700; font-size: 17.5px; line-height: 37.6px; color: var(--ink); }

  /* Picture of the day */
  .photo-frame { left: 56px; top: 232px; width: 328px; height: 218px; border: 1.5px solid var(--panel-line); background: #f2f2f2; }
  .photo { position: absolute; left: 6px; top: 5px; width: 315px; height: 177px;
    background: linear-gradient(180deg, var(--photo-glow) 0%, var(--photo-warm) 55%, #b97a25 100%); }
  .photo-caption { position: absolute; left: 0; right: 0; top: 188px; text-align: center; font-family: "Questrial", sans-serif; font-size: 18px; color: var(--caption); }
  .desc-title { left: 68px; top: 468px; font-weight: 700; font-size: 21px; color: var(--brand-dark); }
  .desc-body { left: 68px; top: 500px; width: 320px; font-family: "Questrial", sans-serif; font-size: 13.6px; line-height: 16px; color: var(--ink-soft); }

  /* Weather */
  .weather { left: 871px; top: 475px; width: 216px; height: 93px; border: 1px solid #9fdcf3;
    background: linear-gradient(180deg, #8fd8f5 0%, #3b8fc6 55%, #2a6f9e 100%); }

  /* Alerts */
  .alerts-bar { left: 53px; top: 587px; width: 1104px; height: 68px; }
  .alerts-tab { left: 43px; top: 594px; width: 133px; height: 34px; gap: 8px; padding-left: 12px; font-size: 26px; border-radius: 10px; }
  .alerts-text { left: 197px; top: 599px; width: 950px; font-family: "Questrial", sans-serif; font-size: 13.8px; line-height: 19.5px; color: var(--ink-soft); }
</style>
</head>
<body>

  <header>
    <div class="abs brand"><span class="brand-dot"></span><span class="brand-name">Vorlan Aerotek</span></div>
    <p class="abs tagline">Progress Shaped By Practice,<br>Quality Shaped By Dedication</p>
    <div class="abs clock"><p>Date:</p><p>Time:</p></div>
  </header>

  <!-- Picture of the Day -->
  <section class="abs panel" style="left:43px;top:177px;width:354px;height:396px;"></section>
  <h2 class="abs band" style="left:65px;top:172px;width:318px;height:48px;padding-left:12px;">
    <span class="band-icon icon-camera" role="img" aria-label="Camera icon"></span>Picture of the Day
  </h2>
  <figure class="abs photo-frame">
    <div class="photo" role="img" aria-label="Picture of the day: airliner on a runway at sunset"></div>
    <figcaption class="photo-caption">&lt; Sample Image &gt;</figcaption>
  </figure>
  <h3 class="abs desc-title">Image brief description</h3>
  <p class="abs desc-body">Lorem ipsum dolor sit amet lorem ipsum dolor sit lor sit amet lorem ipsum dolor sit lorem ipsum lorem ips dolor sum dolor sit amet lorem ipsum.</p>

  <!-- Birthdays -->
  <section class="abs panel" style="left:418px;top:216px;width:353px;height:176px;"></section>
  <h2 class="abs band" style="left:407px;top:171px;width:375px;height:68px;padding-left:26px;align-items:flex-start;padding-top:8px;">
    <span class="band-icon icon-cake" role="img" aria-label="Birthday cake icon"></span>Today’s Birthdays
  </h2>
  <section class="abs panel" style="left:418px;top:216px;width:353px;height:176px;border-top:none;"></section>
  <ul class="abs name-list" style="left:468px;top:227px;">
    <li>First Name, Last Name one</li><li>First Name, Last Name two</li><li>First Name, Last Name three</li><li>First Name, Last Name four</li>
  </ul>

  <!-- Anniversaries -->
  <h2 class="abs band" style="left:792px;top:171px;width:375px;height:68px;padding-left:26px;align-items:flex-start;padding-top:8px;">
    <span class="band-icon icon-glasses" role="img" aria-label="Celebration glasses icon"></span>Today’s Anniversaries
  </h2>
  <section class="abs panel" style="left:803px;top:216px;width:353px;height:176px;border-top:none;"></section>
  <ul class="abs name-list" style="left:853px;top:227px;">
    <li>First Name, Last Name one</li><li>First Name, Last Name two</li><li>First Name, Last Name three</li><li>First Name, Last Name four</li>
  </ul>

  <!-- Visitor -->
  <h2 class="abs band" style="left:407px;top:404px;width:375px;height:67px;padding-left:38px;padding-top:20px;">
    <span class="band-icon icon-card" role="img" aria-label="Visitor card icon"></span>Today’s Visitor
  </h2>
  <div class="abs tab-strip" style="left:418px;top:410px;width:353px;height:18px;"></div>
  <section class="abs panel" style="left:418px;top:471px;width:354px;height:102px;border-top:none;"></section>
  <ul class="abs name-list" style="left:483px;top:487px;">
    <li>First Name, Last Name one</li><li>First Name, Last Name two</li>
  </ul>

  <!-- Weather -->
  <h2 class="abs band" style="left:792px;top:404px;width:375px;height:67px;padding-left:20px;padding-top:20px;">
    <span class="band-icon icon-sun" role="img" aria-label="Sun and cloud icon"></span>Weather Forecast
  </h2>
  <div class="abs tab-strip" style="left:803px;top:410px;width:353px;height:18px;"></div>
  <section class="abs panel" style="left:803px;top:471px;width:353px;height:102px;border-top:none;"></section>
  <div class="abs weather" role="img" aria-label="Weather widget: clock, current conditions and five-day forecast"></div>

  <!-- Alerts -->
  <section class="abs panel alerts-bar"></section>
  <h2 class="abs band alerts-tab">
    <svg width="24" height="22" viewBox="0 0 24 22" aria-hidden="true">
      <path d="M12 1 L23 21 H1 Z" fill="var(--alert-yellow)" stroke="#c98f00" stroke-width="1"/>
      <rect x="10.8" y="7" width="2.4" height="8" rx="1" fill="#222"/>
      <circle cx="12" cy="18" r="1.4" fill="#222"/>
    </svg>Alerts
  </h2>
  <p class="abs alerts-text">Lorem ipsum dolor sit amet lorem ipsum dolor sit lor sit amet lorem ipsum dolor sit lorem ipsum lorem ips dolor sum dolor sit amet lorem ipsum.<br>Lorem ipsum dolor sit amet lorem ipsum dolor sit lor sit amet lorem ipsum dolor sit lorem ipsum lorem ips dolor sum dolor sit amet lorem ipsum.</p>

</body>
</html>
```